Kestrel Bridge Consulting (KBC) Business Card Design

I would like to create double-sided business cards that contain:
1) Name: Derek Molvane
2) Phone Number: +1 (555) 218-4907
3) Email: Derek.Molvane@KestrelBridgeConsulting.example
4) Website: KestrelBridgeConsulting.example

I would like to include my logo and a color scheme similar to the Varnholt Grand Prix Ostera squad color scheme (black, silver, greenish-blue – but can also include regular blue)

What we do: Our company develops and delivers innovative and pragmatic information technology and cybersecurity risk and compliance solutions for organizations in the commercial market as well as the federal, and state/local sectors.

```html
<!DOCTYPE html>
<html lang="en">
<head>
<meta charset="utf-8">
<title>Kestrel Bridge Consulting – Business Cards</title>
<link href="https://fonts.googleapis.com/css2?family=Roboto:wght@400;500;700;900&display=swap" rel="stylesheet">
<style>
  :root {
    --brand-blue: #0b6db0;
    --brand-blue-deep: #0a5f9c;
    --brand-teal: #2bc3c0;
    --ink: #1f2328;
    --text-grey: #555b61;
    --rule-grey: #cfd3d6;
    --paper: #ffffff;
    --backdrop: #2a2c2f;
  }
  * { margin: 0; padding: 0; box-sizing: border-box; }
  html, body {
    width: 1200px; height: 874px; overflow: hidden;
    background: var(--backdrop);
    font-family: "Roboto", Arial, sans-serif;
  }
  .stage {
    position: relative; width: 1200px; height: 874px;
  }
  .card {
    position: absolute; left: 280px; width: 640px; height: 366px;
    border-radius: 22px; overflow: hidden;
  }
  /* Front */
  .card--front { top: 48px; background: var(--brand-blue); }
  .wordmark {
    position: absolute; display: flex; align-items: center; gap: 18px;
  }
  .wordmark__dot {
    width: 74px; height: 74px; border-radius: 50%;
  }
  .wordmark__name {
    font-weight: 500; font-size: 32px; line-height: 1.02;
    letter-spacing: 2px; text-transform: uppercase;
  }
  .card--front .wordmark { left: 132px; top: 112px; }
  .card--front .wordmark__dot { background: var(--paper); }
  .card--front .wordmark__name { color: var(--paper); }
  .card--front .website {
    position: absolute; left: 0; right: 0; bottom: 40px;
    text-align: center; color: var(--paper); font-size: 17px;
  }
  /* Back */
  .card--back { top: 460px; background: var(--paper); }
  .card--back .wordmark { left: 362px; top: 58px; gap: 14px; }
  .card--back .wordmark__dot { width: 58px; height: 58px; background: var(--brand-teal); }
  .card--back .wordmark__name { color: var(--ink); font-size: 24px; }
  .side-tab {
    position: absolute; left: 0; top: 134px; width: 16px; height: 40px;
    background: var(--brand-blue);
  }
  .contact { position: absolute; left: 44px; top: 130px; }
  .contact__name {
    color: var(--brand-blue); font-weight: 900; font-size: 30px;
    letter-spacing: 0.5px; text-transform: uppercase;
  }
  .contact__role { color: var(--text-grey); font-size: 16px; margin-top: 2px; }
  .rule {
    position: absolute; left: 44px; right: 44px; top: 212px;
    height: 1px; background: var(--rule-grey);
  }
  .details { position: absolute; left: 44px; top: 224px; color: var(--text-grey); font-size: 16px; }
  .details__line { display: flex; align-items: center; gap: 8px; height: 24px; }
  .details__line svg { width: 14px; height: 14px; flex: none; }
  .footer-bands { position: absolute; left: 0; bottom: 0; width: 640px; height: 70px; }
  .card--back .website {
    position: absolute; right: 36px; bottom: 12px;
    color: var(--paper); font-size: 17px; font-weight: 500;
  }
</style>
</head>
<body>
<main class="stage">
  <section class="card card--front" aria-label="Business card front">
    <div class="wordmark">
      <span class="wordmark__dot"></span>
      <span class="wordmark__name">Kestrel<br>Bridge<br>Consulting</span>
    </div>
    <p class="website">www.KestrelBridgeConsulting.example</p>
  </section>

  <section class="card card--back" aria-label="Business card back">
    <div class="wordmark">
      <span class="wordmark__dot"></span>
      <span class="wordmark__name">Kestrel<br>Bridge<br>Consulting</span>
    </div>
    <span class="side-tab"></span>
    <div class="contact">
      <h1 class="contact__name">Derek Molvane</h1>
      <p class="contact__role">President</p>
    </div>
    <div class="rule"></div>
    <div class="details">
      <p class="details__line">
        <svg viewBox="0 0 24 24" aria-hidden="true"><path fill="#2bc3c0" d="M6.6 10.8a15.1 15.1 0 0 0 6.6 6.6l2.2-2.2a1 1 0 0 1 1-.25 11.4 11.4 0 0 0 3.6.57 1 1 0 0 1 1 1V20a1 1 0 0 1-1 1A17 17 0 0 1 3 4a1 1 0 0 1 1-1h3.5a1 1 0 0 1 1 1c0 1.25.2 2.45.57 3.57a1 1 0 0 1-.25 1z"/></svg>
        +1 (555) 218-4907
      </p>
      <p class="details__line">
        <svg viewBox="0 0 24 24" aria-hidden="true"><rect x="2" y="5" width="20" height="14" rx="2" fill="#2bc3c0"/><path d="M3 6l9 7 9-7" fill="none" stroke="#fff" stroke-width="1.8"/></svg>
        Derek.Molvane@KestrelBridgeConsulting.example
      </p>
      <p class="details__line">
        <svg viewBox="0 0 24 24" aria-hidden="true"><path fill="#2bc3c0" d="M12 2a7 7 0 0 0-7 7c0 5 7 13 7 13s7-8 7-13a7 7 0 0 0-7-7zm0 9.5A2.5 2.5 0 1 1 12 6.5a2.5 2.5 0 0 1 0 5z"/></svg>
        412 Harbor Row, Northfield, Canada 20817
      </p>
    </div>
    <svg class="footer-bands" viewBox="0 0 640 70" preserveAspectRatio="none" aria-hidden="true">
      <polygon points="0,18 330,18 318,36 0,36" fill="#2bc3c0"/>
      <polygon points="0,36 318,36 330,30 640,30 640,70 0,70" fill="#0b6db0"/>
    </svg>
    <p class="website">www.KestrelBridgeConsulting.example</p>
  </section>
</main>
</body>
</html>
```